Brocure for Brindle - Social Media Management

Brindle is a Dutch company in the market of Social Media growth. We need a brochure (digital/PDF) for our company. Please see attached word doc for the text and attached logo. The initial proposal can contain just the first 4 pages text of the word doc.

We use informal language in all our communication.

Slogan: Effectieve Social Media Marketing voor professionals en ondernemers

Website: brindlesm-voorbeeld.nl

Industry/Entity Type

Digital Marketing

Contact Information for Business Card

Contact details:

Gerrit ter Hoeve
gerrit@brindlesm-voorbeeld.nl
06-19573826

```html
<!DOCTYPE html>
<html lang="nl">
<head>
<meta charset="utf-8">
<title>Brindle – Effectieve Social Media Marketing</title>
<link href="https://fonts.googleapis.com/css2?family=Poppins:ital,wght@0,600;0,700;1,800&display=swap" rel="stylesheet">
<style>
  :root {
    --navy: #14264a;
    --navy-deep: #0f1f3d;
    --navy-soft: #2a3d5e;
    --orange: #f26a2e;
    --orange-deep: #d45a2c;
    --orange-light: #f5843e;
    --white: #ffffff;
    --grey-text: #878787;
    --paper: #f3f3f3;
  }
  html, body {
    margin: 0;
    padding: 0;
    width: 1200px;
    height: 1200px;
    overflow: hidden;
    background: var(--navy);
  }
  .cover {
    position: relative;
    width: 1200px;
    height: 1200px;
    overflow: hidden;
    font-family: "Poppins", Arial, sans-serif;
  }
  .cover-shapes {
    position: absolute;
    inset: 0;
  }
  .headline {
    position: absolute;
    left: 34px;
    top: 606px;
    margin: 0;
    font-style: italic;
    font-weight: 800;
    font-size: 61px;
    line-height: 81px;
    letter-spacing: 0.3px;
    color: var(--white);
  }
  .headline span { display: block; white-space: nowrap; }
  .headline .accent { color: var(--orange); }
  .headline .muted { color: var(--grey-text); }
  .brand {
    position: absolute;
    left: 850px;
    top: 1020px;
    display: flex;
    align-items: center;
    gap: 14px;
  }
  .brand-dot {
    width: 44px;
    height: 44px;
    border-radius: 50%;
    background: var(--navy);
  }
  .brand-name {
    font-family: "Poppins", Arial, sans-serif;
    font-weight: 700;
    font-size: 62px;
    line-height: 1;
    letter-spacing: 2px;
    color: var(--orange);
  }
</style>
</head>
<body>
<main class="cover">
  <svg class="cover-shapes" width="1200" height="1200" viewBox="0 0 1200 1200">
    <defs>
      <linearGradient id="photoTone" x1="0" y1="0" x2="1" y2="1">
        <stop offset="0" stop-color="#1a2d50"/>
        <stop offset="0.5" stop-color="#223758"/>
        <stop offset="1" stop-color="#12223f"/>
      </linearGradient>
      <linearGradient id="cornerOrange" x1="0" y1="0" x2="1" y2="0">
        <stop offset="0" stop-color="var(--orange-light)"/>
        <stop offset="1" stop-color="var(--orange)"/>
      </linearGradient>
      <linearGradient id="sideOrange" x1="0" y1="0" x2="0" y2="1">
        <stop offset="0" stop-color="#c9512a"/>
        <stop offset="1" stop-color="#dd6636"/>
      </linearGradient>
    </defs>

    <rect class="background-photo" width="1200" height="1200" fill="url(#photoTone)"
          role="img" aria-label="Dark navy photo of stacked cubes with social media icons"/>

    <polygon class="corner-triangle" points="0,0 323,0 0,323" fill="url(#cornerOrange)"/>
    <polygon class="side-band" points="1200,14 835,835 1200,752" fill="url(#sideOrange)"/>
    <polygon class="bottom-band" points="0,1200 835,835 752,1200" fill="var(--orange-deep)" fill-opacity="0.72"/>
    <polygon class="engagement-panel" points="835,835 1200,752 1200,1200 752,1200" fill="var(--paper)"
             role="img" aria-label="Faint light photo of social media notification bubbles with like and follower counts"/>
  </svg>

  <h1 class="headline">
    <span class="accent">Effectieve</span>
    <span>Social Media Marketing</span>
    <span>Voor Professionals En</span>
    <span class="muted">Ondernemers</span>
  </h1>

  <div class="brand">
    <div class="brand-dot"></div>
    <div class="brand-name">Brindle</div>
  </div>
</main>
</body>
</html>
```